Unit 24 Maple Ridge

We want a postcard with a picture of the property that was just sold and comments from the seller on the front of the postcard. " After experiencing the level of service of many realtors in your area, you and your staff are a breath of fresh air. Garrick, you have presented yourself in a professional manner, with progressive ideas as to how to handle our listings. You and Lorna have proven to be ambitious, handling our listings with skill and a positive work ethic" On the back we have standard verbiage that we want to use.

I have attached a copy of what we want on the back of the card.

Target Market(s)

We are sending a postcard to everyone who lives on Bramwell Pond because if they are thinking of selling we want them to list with us.

Industry/Entity Type

Progressive

Font styles to use
Sans Serif

Colors
85acd3
33a6d7
86cfc6

```html
<!DOCTYPE html>
<html lang="en">
<head>
<meta charset="utf-8">
<title>Bramwell Pond Land &amp; Home – Postcard</title>
<link href="https://fonts.googleapis.com/css2?family=Questrial&family=Mr+De+Haviland&display=swap" rel="stylesheet">
<style>
  :root {
    --page: #ffffff;
    --ink: #3a3a3a;
    --ink-soft: #555555;
    --brand-brown: #4a3a2c;
    --sky: #3f8fd6;
    --sky-light: #85acd3;
    --water: #5b7f92;
    --forest: #2f4a2a;
    --lawn: #4f8a2e;
    --aqua: #86cfc6;
    --rule: #5a4636;
    --icon: #444444;
  }
  * { box-sizing: border-box; margin: 0; padding: 0; }
  html, body { width: 979px; height: 1200px; overflow: hidden; background: var(--page); }
  body { position: relative; font-family: "Questrial", "Century Gothic", sans-serif; color: var(--ink); }

  .card { position: absolute; left: 82px; width: 792px; background: var(--page); overflow: hidden; outline: 1px solid #e4e4e4; }
  .card--front { top: 46px; height: 512px; }
  .card--back { top: 620px; height: 508px; }

  /* Front */
  .front__photo {
    position: absolute; left: 0; top: 0; width: 792px; height: 393px;
    background: linear-gradient(180deg, var(--sky) 0%, var(--sky-light) 30%, var(--forest) 38%, #3e5a38 44%, var(--water) 50%, #6f8fa0 80%, #5f7e8c 100%);
  }
  .front__photo-lawn {
    position: absolute; right: 0; top: 150px; width: 150px; height: 243px;
    background: linear-gradient(160deg, #c9b9a0 0%, #b8a58a 40%, var(--lawn) 60%, #3f7a25 100%);
  }
  .brand-mark {
    position: absolute; left: 34px; top: 368px; width: 264px; height: 122px;
    display: flex; flex-direction: column; align-items: center; justify-content: center;
    background: var(--page); border-radius: 50%;
    color: var(--brand-brown); text-align: center; line-height: 1.1;
  }
  .brand-mark__name { font-size: 27px; letter-spacing: 1px; }
  .brand-mark__sub { font-size: 15px; letter-spacing: 2px; margin-top: 4px; }
  .front__quote {
    position: absolute; left: 363px; top: 402px; width: 418px;
    font-size: 12.6px; line-height: 1.22; color: var(--ink);
  }

  /* Back */
  .back__photo {
    position: absolute; left: 344px; top: 0; width: 448px; height: 508px;
    background: linear-gradient(180deg, #dbe7f2 0%, #d6d0c2 30%, #c4b7a0 50%, var(--lawn) 70%, #8a9aa4 100%);
  }
  .back__photo-fade {
    position: absolute; left: 0; top: 0; width: 792px; height: 508px;
    background: linear-gradient(90deg, var(--page) 0%, var(--page) 44%, rgba(255,255,255,0.85) 56%, rgba(255,255,255,0.2) 75%, rgba(255,255,255,0) 90%);
  }
  .back__lower-fade {
    position: absolute; left: 120px; top: 300px; width: 330px; height: 208px;
    background: linear-gradient(90deg, rgba(255,255,255,0) 0%, rgba(180,190,196,0.25) 60%, rgba(255,255,255,0) 100%);
  }
  .pitch { position: absolute; left: 32px; top: 46px; width: 302px; }
  .pitch__title { font-size: 16.8px; line-height: 1.2; font-weight: 400; color: var(--ink); }
  .pitch__body { font-size: 11.4px; line-height: 1.3; color: var(--ink); }
  .pitch__link { color: #8a8a8a; font-size: 13px; }
  .divider { position: absolute; left: 344px; top: 38px; width: 2px; height: 428px; background: var(--rule); }

  .invite { position: absolute; left: 36px; top: 350px; width: 290px; font-size: 15.3px; line-height: 1.25; color: var(--ink); }
  .signature { position: absolute; left: 30px; top: 424px; font-family: "Mr De Haviland", cursive; font-size: 42px; color: var(--brand-brown); }
  .quick-contact { position: absolute; left: 146px; top: 436px; font-size: 11.6px; line-height: 1.6; color: var(--ink-soft); }

  .back-brand { position: absolute; left: 376px; top: 26px; width: 246px; height: 112px; display: flex; flex-direction: column; align-items: center; justify-content: center; border-radius: 50%; background: rgba(255,255,255,0.85); color: var(--brand-brown); text-align: center; line-height: 1.1; }
  .back-brand .brand-mark__name { font-size: 24px; }
  .back-brand .brand-mark__sub { font-size: 13px; }

  .contact { position: absolute; left: 362px; top: 170px; font-size: 11.4px; color: var(--ink-soft); }
  .contact__row { display: flex; align-items: center; gap: 10px; margin-bottom: 6px; }
  .contact__row svg { flex: none; }
  .contact__block { margin-left: 24px; line-height: 1.5; }
  .contact__heading { font-size: 15px; color: var(--ink); margin: 6px 0 6px 24px; }
  .badges { display: flex; gap: 6px; margin-top: 18px; }
  .badge { width: 16px; height: 14px; background: var(--icon); }
</style>
</head>
<body>

<section class="card card--front">
  <div class="front__photo" role="img" aria-label="Lakefront condominium with boat docks and moored boats on calm blue water under a sunny sky">
    <div class="front__photo-lawn"></div>
  </div>
  <div class="brand-mark">
    <span class="brand-mark__name">BRAMWELL POND</span>
    <span class="brand-mark__sub">LAND &amp; HOME</span>
  </div>
  <p class="front__quote">" After experiencing the level of service of many realtors in your area, you and your staff are a breath of fresh air. Garrick, you have presented yourself in a professional manner, with progressive ideas as to how to handle our listings. You and Lorna have proven to be ambitious, handling our listings with skill and a positive work ethic"</p>
</section>

<section class="card card--back">
  <div class="back__photo" role="img" aria-label="Lakeside condominium building with green lawn and boat docks, fading into white"></div>
  <div class="back__photo-fade"></div>
  <div class="back__lower-fade"></div>

  <div class="pitch">
    <h2 class="pitch__title">There is a big difference between listing a home and selling it.</h2>
    <p class="pitch__body">At Bramwell Pond Land &amp; Home we understand this difference. The key is knowing how to position your property to get the attention of those buyers who are truly motivated and qualified in your price range. Bramwell Pond real estate is a unique, micro market within our MLS and that is why we created our waterfront only website, <span class="pitch__link">www.bramwellpondhomes.com</span>, to target lakefront buyers. If you are not supported by the right game plan, the right agent, and the right company... you are going to have already experienced. My team and I don't just list your home, we market it aggressively and consistently to your target market and get it sold!<br>We create a terrific Internet presence for your property, showcasing your property's special attributes.<br>Our goal is to dominate competing listing with our marketing!</p>
  </div>

  <div class="divider"></div>

  <p class="invite">Please call me, I would love the opportunity to present you with a marketing plan designed specifically for your property!</p>
  <div class="signature">Garrick</div>
  <div class="quick-contact">
    <div class="contact__row">
      <svg width="10" height="14" viewBox="0 0 10 14"><rect x="1" y="0.5" width="8" height="13" rx="1.5" fill="none" stroke="var(--icon)" stroke-width="1.2"/><circle cx="5" cy="11.3" r="0.9" fill="var(--icon)"/></svg>
      <span>406-555-0148</span>
    </div>
    <div class="contact__row">
      <svg width="12" height="12" viewBox="0 0 12 12"><circle cx="6" cy="6" r="5.3" fill="none" stroke="var(--icon)" stroke-width="1.1"/><ellipse cx="6" cy="6" rx="2.3" ry="5.3" fill="none" stroke="var(--icon)" stroke-width="1"/><line x1="0.7" y1="6" x2="11.3" y2="6" stroke="var(--icon)"/></svg>
      <span>www.bramwellpondhomes.com</span>
    </div>
  </div>

  <div class="back-brand">
    <span class="brand-mark__name">BRAMWELL POND</span>
    <span class="brand-mark__sub">LAND &amp; HOME</span>
  </div>

  <div class="contact">
    <div class="contact__row">
      <svg width="12" height="16" viewBox="0 0 12 16"><path d="M6 15 C2 9.5 1 7.5 1 5.5 A5 5 0 0 1 11 5.5 C11 7.5 10 9.5 6 15 Z" fill="var(--icon)"/><circle cx="6" cy="5.5" r="2" fill="#fff"/></svg>
      <span>Bramwell Pond Land &amp; Home</span>
    </div>
    <div class="contact__block">1740 Harbor View Rd<br>Alderton, MT 59000</div>
    <div class="contact__row" style="margin-top:4px">
      <svg width="13" height="13" viewBox="0 0 12 12"><circle cx="6" cy="6" r="5.3" fill="none" stroke="var(--icon)" stroke-width="1.1"/><ellipse cx="6" cy="6" rx="2.3" ry="5.3" fill="none" stroke="var(--icon)" stroke-width="1"/><line x1="0.7" y1="6" x2="11.3" y2="6" stroke="var(--icon)"/></svg>
      <span>www.bramwellpondhomes.com</span>
    </div>
    <div class="contact__heading">Contact Garrick Holloway</div>
    <div class="contact__row">
      <svg width="13" height="15" viewBox="0 0 10 14"><rect x="1" y="0.5" width="8" height="13" rx="1.5" fill="none" stroke="var(--icon)" stroke-width="1.2"/><circle cx="5" cy="11.3" r="0.9" fill="var(--icon)"/></svg>
      <span>406-555-0148</span>
    </div>
    <div class="contact__row">
      <svg width="13" height="10" viewBox="0 0 13 10"><rect x="0" y="0" width="13" height="10" fill="var(--icon)"/><path d="M0.5 0.5 L6.5 5.5 L12.5 0.5" fill="none" stroke="#fff" stroke-width="1"/></svg>
      <span>garrick@bramwellpondhomes.com</span>
    </div>
    <div class="badges">
      <span class="badge"></span>
      <span class="badge"></span>
      <span class="badge" style="width:18px"></span>
    </div>
  </div>
</section>

</body>
</html>
```